Quick Straightforward Billboard Redesign

- Design billboard sized for 10 foot' x 36' foot width live area size and please include bleeds 6" around all sides
- Exact blue color match is imperative in headline, logo, phone number bubble or wherever used. C-83 / M-45 / Y-1 / K-0-
- What I hope to illustrate is that our company offers the best porch screening in the area area, in regards to quality, expertise, durability, storms proof, but we do not build screen porches.
- Current board is attached below from previous designer, and as you can see sizing was off, white space on edges make it appear to be sized incorrectly.
- I also attached my own little mock up idea well well if it helps, favorite image, logo, headline, etc and ideas perhaps on expanding or making this better?

Thanks so much!

Target Market(s)

Drivers and passengers, Southeastern NC, are of immense new construction and high end homes.

Industry/Entity Type

Construction

Colors
0054AA
0677BA
7BADD7
CADEEF
E8F1F8

Requirements
Must have
• Blue color matching
Nice to have
• Design spins or other thoughts on my little mock up

```html
<!DOCTYPE html>
<html lang="en">
<head>
<meta charset="utf-8">
<title>Tidewater Mesh Co. Billboard</title>
<link href="https://fonts.googleapis.com/css2?family=Antonio:wght@700&family=Bebas+Neue&display=swap" rel="stylesheet">
<style>
  :root {
    --band-blue: #03548a;
    --brand-blue: #0e6db8;
    --accent-green: #27b35a;
    --sky-blue: #1b86cc;
    --paper: #ffffff;
    --backdrop: #d9d9d9;
    --photo-sky: #8fbfe6;
    --photo-grass: #9cc27a;
    --photo-floor: #d9d3c8;
  }
  * { margin: 0; padding: 0; box-sizing: border-box; }
  html, body {
    width: 1200px; height: 420px; overflow: hidden;
    background: var(--backdrop);
  }
  .billboard {
    position: absolute; left: 39px; top: 55px;
    width: 1106px; height: 307px;
    background: var(--paper);
    overflow: hidden;
  }
  .hero-band {
    position: absolute; left: 0; top: 0;
    width: 100%; height: 215px;
    background: var(--band-blue);
  }
  .hero-art {
    position: absolute; left: 0; top: 0;
    width: 1106px; height: 215px;
  }
  .headline {
    position: absolute; left: 44px; top: 16px;
    font-family: "Bebas Neue", sans-serif;
    font-weight: 400;
    font-size: 100px; line-height: 87px;
    letter-spacing: 0.5px;
    white-space: nowrap;
  }
  .headline-top { color: var(--paper); display: block; }
  .headline-bottom { color: var(--accent-green); display: block; }
  .footer-band {
    position: absolute; left: 0; top: 215px;
    width: 100%; height: 92px;
  }
  .brand {
    position: absolute; left: 45px; top: 16px;
    height: 60px;
    display: flex; align-items: center; gap: 16px;
    white-space: nowrap;
  }
  .brand-square {
    width: 44px; height: 44px;
    background: var(--brand-blue);
    flex: none;
  }
  .brand-name {
    font-family: "Bebas Neue", sans-serif;
    font-size: 67px; line-height: 60px;
    color: var(--brand-blue);
    padding-top: 6px;
  }
  .contact {
    position: absolute; right: 36px; top: 16px;
    height: 60px;
    display: flex; align-items: center; gap: 12px;
    white-space: nowrap;
  }
  .phone-badge { width: 44px; height: 44px; flex: none; }
  .contact-number {
    font-family: "Antonio", sans-serif; font-weight: 700;
    font-size: 54px; line-height: 60px;
    color: var(--brand-blue);
    letter-spacing: 0;
  }
</style>
</head>
<body>
  <main class="billboard">
    <section class="hero-band">
      <svg class="hero-art" viewBox="0 0 1106 215" xmlns="http://www.w3.org/2000/svg">
        <defs>
          <linearGradient id="porchTones" x1="0" y1="0" x2="0" y2="1">
            <stop offset="0" stop-color="#f1f1ef"/>
            <stop offset="0.2" stop-color="#8fbfe6"/>
            <stop offset="0.5" stop-color="#9cc27a"/>
            <stop offset="0.62" stop-color="#8a7a66"/>
            <stop offset="1" stop-color="#d9d3c8"/>
          </linearGradient>
        </defs>
        <polygon points="720,0 760,112 717,215 734,215 774,112 736,0" fill="#27b35a"/>
        <polygon points="760,112 774,112 734,215 717,215" fill="#1b86cc"/>
        <polygon points="736,0 1106,0 1106,215 734,215 774,112" fill="url(#porchTones)" role="img" aria-label="Photo of a screened coastal porch with wicker seating, ceiling fan and a lake view"/>
      </svg>
      <h1 class="headline">
        <span class="headline-top">Screen your porch.</span>
        <span class="headline-bottom">Built for the coast.</span>
      </h1>
    </section>
    <section class="footer-band">
      <div class="brand">
        <span class="brand-square"></span>
        <span class="brand-name">TIDEWATER MESH CO.</span>
      </div>
      <div class="contact">
        <svg class="phone-badge" viewBox="0 0 44 44" xmlns="http://www.w3.org/2000/svg" aria-hidden="true">
          <circle cx="22" cy="22" r="20.5" fill="none" stroke="#0e6db8" stroke-width="1.5"/>
          <path d="M15 14c1.5-1.5 3-1.3 3.8.2l1.4 2.6c.6 1.1.3 2-.6 2.7l-1 .8c.8 2 2.5 3.8 4.6 4.8l.9-1c.8-.9 1.7-1.1 2.7-.5l2.6 1.5c1.4.8 1.5 2.4.1 3.8-1.6 1.6-4 2-6.4.8-4.1-2-7.4-5.4-9-9.6-.9-2.4-.5-4.5.9-6.1z" fill="#03548a"/>
          <path d="M23 14.5a6 6 0 0 1 6 6M23 11a9.5 9.5 0 0 1 9.5 9.5" fill="none" stroke="#27b35a" stroke-width="1.6" stroke-linecap="round"/>
        </svg>
        <span class="contact-number">Call 910.555.0142</span>
      </div>
    </section>
  </main>
</body>
</html>
```